Cedar nest sal
Affordable luxury
Professional
Paul dorsey
Doesn't matter, just write anything, will finalize later
Pauldorsey@quillmarsh.net
All I need is a template that suits the logo, I expect a draft template from your side.
It should include, the name, title, company logo, subtitle, website address, physical address, phone number and email. Thank you
Please suggest
Design number 1 will be used
red as second option

```html
<!DOCTYPE html>
<html lang="en">
<head>
<meta charset="utf-8">
<title>Cedar Nest Sal – Business Card</title>
<link rel="stylesheet" href="https://fonts.googleapis.com/css2?family=Arimo:wght@400;700&display=swap">
<style>
  :root {
    --stage: #2a2422;
    --card: #ffffff;
    --brand-green: #0f8a3b;
    --brand-brown: #6e3b1f;
    --text-light: #ffffff;
  }
  * { margin: 0; padding: 0; box-sizing: border-box; }
  html, body { width: 1200px; height: 475px; overflow: hidden; }
  body {
    background: var(--stage);
    font-family: "Arimo", Arial, sans-serif;
    position: relative;
  }
  .card {
    position: absolute;
    top: 89px;
    width: 512px;
    height: 290px;
    background: var(--card);
    border-radius: 16px;
    overflow: hidden;
  }
  .card--front { left: 72px; }
  .card--back { left: 606px; }

  .wordmark {
    position: absolute;
    display: flex;
    align-items: center;
    gap: 8px;
    color: var(--brand-brown);
    font-weight: 700;
    letter-spacing: 0.5px;
    white-space: nowrap;
    transform: translate(-50%, -50%);
  }
  .wordmark__mark {
    width: 14px;
    height: 14px;
    background: var(--brand-brown);
  }
  .card--front .wordmark { left: 144px; top: 160px; font-size: 24px; }
  .card--back .wordmark { left: 256px; top: 145px; font-size: 26px; }

  .contact-panel {
    position: absolute;
    left: 283px;
    top: 0;
    width: 229px;
    height: 290px;
    background: var(--brand-green);
    border-radius: 16px;
    color: var(--text-light);
  }
  .contact-panel__name,
  .contact-panel__role {
    text-align: center;
    font-weight: 700;
    font-size: 19px;
    line-height: 24px;
  }
  .contact-panel__name { margin-top: 46px; }
  .contact-panel__details {
    position: absolute;
    left: 58px;
    top: 144px;
    font-size: 13px;
    line-height: 17px;
    list-style: none;
  }
</style>
</head>
<body>
  <section class="card card--front">
    <div class="wordmark"><span class="wordmark__mark"></span>Cedar Nest Sal</div>
    <div class="contact-panel">
      <p class="contact-panel__name">Paul Dorsey</p>
      <p class="contact-panel__role">Owner</p>
      <ul class="contact-panel__details">
        <li>Via Lorenzo Bassi 14</li>
        <li>20131 Milano</li>
        <li>+39.02.48217063</li>
        <li>+39.348.5520917</li>
        <li>+39.02.48217063</li>
        <li>info@quillmarsh.net</li>
      </ul>
    </div>
  </section>

  <section class="card card--back">
    <div class="wordmark"><span class="wordmark__mark"></span>Cedar Nest Sal</div>
  </section>
</body>
</html>
```